Towing company card on one side and our Autobody and collision repair shop card on the other

We need a two sided business card on one side it would be for our towing company and the other for our auto body and collision repair shop we would like our logo to appear on the card on the autobody shop side .I would like the card to be unique not just a regular towing or auto body shop company card. Our tow truck company offers flatbed and wheel lift service short and long distance we also offer roadside assistance which covers jumpstarts, tire changes, lock outs we are on call 24/7. All of our trucks are state of the art and brand new with air ride suspension and low profile beds. The phone number for the towing company is 201-574-3902. We accept all major credit cards. The other side of the card would be for the Auto body shop specializing in auto painting, body and fender repair, frame straightening , unibody repair and fiberglass repair work. We color match factory paint and we handle all insurance companies claims.The phone number for the auto body shop is 201-368-2915 fax 201-368-2915 email redfinchautobody@mailvale.net the autobody license number must appear on the autobody side of the card in this format. LIC#04817C

Target Market(s)

new customers

Industry/Entity Type

Business

Contact Information for Business Card

towing company on one side and auto body and collision repair on the other side

Colors
ec1f27
000000
aaaaaa
e9e9e9
0555a3
959595
1b1b1b

Requirements
Must have
• Must have company logo on card on the autobody side of card and show address 4816 Garvick ave Eastwood NJ 07391

```html
<!DOCTYPE html>
<html lang="en">
<head>
<meta charset="utf-8">
<title>Red Finch Auto Body &amp; Towing – Business Card</title>
<link href="https://fonts.googleapis.com/css2?family=Lato:wght@400;700;900&display=swap" rel="stylesheet">
<style>
  :root{
    --red:#ec1f27;
    --black:#000000;
    --ink:#1b1b1b;
    --grey:#aaaaaa;
    --grey-dark:#959595;
    --paper:#e9e9e9;
    --white:#f7f7f7;
    --stage:#d9d9d9;
  }
  *{box-sizing:border-box;margin:0;padding:0}
  html,body{width:1200px;height:900px;overflow:hidden}
  body{
    background:var(--stage);
    font-family:"Lato",Arial,sans-serif;
    display:flex;align-items:center;justify-content:center;gap:40px;
  }
  .card{
    position:relative;width:540px;height:310px;
    box-shadow:0 10px 24px rgba(0,0,0,.25);
    overflow:hidden;
  }
  .brand{
    display:flex;align-items:center;gap:8px;
    font-weight:900;letter-spacing:.5px;text-transform:uppercase;white-space:nowrap;
  }
  .brand__dot{width:12px;height:12px;border-radius:50%;background:var(--red);flex:none}

  /* Auto body side */
  .card--autobody{background:linear-gradient(160deg,#1f1f1f,#0a0a0a);color:var(--white)}
  .card--autobody .brand{position:absolute;top:26px;right:60px;font-size:22px;color:var(--white)}
  .license{position:absolute;top:94px;left:26px;font-size:14px;color:var(--white)}
  .license span{color:var(--red)}
  .tagline{
    position:absolute;top:82px;right:26px;width:340px;text-align:center;
    color:var(--red);font-size:13px;font-weight:700;line-height:1.35;text-transform:uppercase;
  }
  .rule{position:absolute;height:1px;background:#555}
  .rule--top{top:126px;left:200px;right:26px}
  .rule--mid{top:232px;left:26px;right:300px}
  .contacts{position:absolute;top:138px;left:26px;list-style:none;font-size:16px;line-height:1.35}
  .contacts li{display:flex;align-items:center;gap:7px;white-space:nowrap}
  .contacts .contacts__address{font-size:14px}
  .contacts svg{width:13px;height:13px;fill:var(--red);flex:none}
  .services{position:absolute;top:242px;left:26px;right:20px;list-style:none;font-size:13px;line-height:1.6;color:var(--white)}
  .services li{display:inline}
  .services li::before{content:"";display:inline-block;width:7px;height:7px;border-radius:50%;background:var(--red);margin:0 6px 1px 0}
  .services li+li{margin-left:8px}
  .services .break{display:block;height:0}

  /* Towing side */
  .card--towing{background:var(--white);color:var(--ink)}
  .card--towing .brand{position:absolute;top:34px;right:70px;font-size:20px;color:var(--ink)}
  .features{position:absolute;top:118px;left:40px;right:40px;list-style:none;font-size:12.5px;line-height:1.55}
  .features li{position:relative;padding-left:14px}
  .features li::before{content:"";position:absolute;left:0;top:6px;width:7px;height:7px;border-radius:50%;background:var(--red)}
  .band{
    position:absolute;left:0;right:0;bottom:0;height:70px;background:var(--ink);
    display:flex;align-items:center;justify-content:space-between;padding:0 40px;font-size:15px;
  }
  .band__call{color:var(--red);font-weight:700;text-transform:uppercase}
  .band__phone{color:var(--white)}
  .band__phone span{color:var(--red);margin-right:6px}
</style>
</head>
<body>

<section class="card card--autobody" aria-label="Auto body side">
  <div class="brand"><span class="brand__dot"></span>Red Finch Auto Body &amp; Towing</div>
  <p class="license"><span>LIC</span>#04817C</p>
  <p class="tagline">We color match factory paint and we<br>handle all insurance companies claims</p>
  <div class="rule rule--top"></div>
  <ul class="contacts">
    <li><svg viewBox="0 0 24 24" aria-hidden="true"><path d="M6.6 10.8a15 15 0 0 0 6.6 6.6l2.2-2.2a1 1 0 0 1 1-.25 11.4 11.4 0 0 0 3.6.57 1 1 0 0 1 1 1V20a1 1 0 0 1-1 1A17 17 0 0 1 3 4a1 1 0 0 1 1-1h3.5a1 1 0 0 1 1 1c0 1.25.2 2.45.57 3.6a1 1 0 0 1-.25 1z"/></svg>201-368-2915</li>
    <li><svg viewBox="0 0 24 24" aria-hidden="true"><path d="M6 2h10v6H6zM3 9h18v9h-3v4H6v-4H3zm5 7v4h8v-4z"/></svg>201-368-2915</li>
    <li><svg viewBox="0 0 24 24" aria-hidden="true"><path d="M2 5h20v14H2zm2 2v.5l8 5 8-5V7z"/></svg>redfinchautobody@mailvale.net</li>
    <li class="contacts__address"><svg viewBox="0 0 24 24" aria-hidden="true"><path d="M12 2a7 7 0 0 0-7 7c0 5 7 13 7 13s7-8 7-13a7 7 0 0 0-7-7zm0 9.5A2.5 2.5 0 1 1 12 6.5a2.5 2.5 0 0 1 0 5z"/></svg>4816 Garvick ave Eastwood NJ 07391</li>
  </ul>
  <div class="rule rule--mid"></div>
  <ul class="services">
    <li>Auto painting</li><li>Body and fender repair</li><span class="break"></span>
    <li>Frame straightening</li><li>Unibody repair and fiberglass repair work.</li>
  </ul>
</section>

<section class="card card--towing" aria-label="Towing side">
  <div class="brand"><span class="brand__dot"></span>Red Finch Auto Body &amp; Towing</div>
  <ul class="features">
    <li>Flatbed and wheel lift service short and long distance.</li>
    <li>we also offer roadside assistance which covers jumpstarts, tire change outs and lock outs.</li>
    <li>Our trucks are state of the art and brand new with air ride suspension and low profile beds.</li>
    <li>We accept all major credit cards.</li>
  </ul>
  <div class="band">
    <p class="band__call">We are on call 24/7.</p>
    <p class="band__phone"><span>Phone</span>201-574-3902</p>
  </div>
</section>

</body>
</html>
```